International Financial Organization needs a new Digital Workplace home page design

We need creative designs for the new Digital Workplace that will replace the current Intranet for an international organization based in Washington DC.

Organization Background: An organization of 189 countries, working to foster global monetary cooperation, secure financial stability, facilitate international trade, promote high employment and sustainable economic growth, and reduce poverty around the world.

Digital Workplace: The Digital workplace will be the central location that allows employees to do their work in productive, simple, and integrated manner.
Knowledge and Information are the lifeblood of our organization. Economists and experts conduct a lot of data-heavy research and produce a lot of reports and documents. The digital workplace will need to facilitate sharing of knowledge and collaboration among employees, and save them the hassle from going to multiple digital locations to do their work. Therefore the seamless integration of systems, and mobile-first design, is key.

Country Missions: A number of our economists travel on "missions" to countries all over the world on periodic basis to meet with country officials, present and discuss findings, and provide consultation. Before they go on missions, these economist do a lot of preparation and research about that country, and they collaborate in teams. When on mission (sometimes in areas that have very limited bandwidth connectivity) they need access to their documents, research, and resources and they need to collaborate with one another. Therefore mobility (zelkorm, tavlo, laptop and desktops) and personalization are very important design criteria. When they are back from their mission they need to document reports and findings, and they will need to work on that through multiple systems.

Design Concept: We attach a concept of the digital workplace homepage (power point slides). The concept offers three views (the three tabs at the top: Enterprise View, Departmental View, and My View.)
The enterprise view is meant to be for all the users in the organization, and displays information that the org want to push to all employees. Not much of personalization is listed in this this view. We only provide the name of potential tiles there. Please be creative and think out of the box, we are open for ideas. The second view is the departmental view. It is meant to focus on the news, events, and information that the department want to share with me as an employee of that department. We only provide the name of potential tiles there. Please be creative and think out of the box, we are open for ideas.
Finally, “My View” is illustrated with sample tiles of what we envision to be used there. We provide two variations for our vision of the “My View”. The tiles that are listed there are not meant to be in that same exact location. Please feel free to change the groupings of these tiles as the page allows (We had to fit our design on 16:9 PPT slide so it’s a not a real page). Also, these tiles are not mean to be restrictive, please be creative and suggest other tiles as you’d envision a modern Digital Workplace. We are open for ideas!

Deliverables: we expect to see at least one creative design per each of these 3 views of the home page for desktop view, and the equivalent in mobile view. In addition we expect any other views/variations that your creativity inspires.

Preferred color pallet: blue, green, orange, and all their gradients. Also open for other colors as your creativity inspires for an established, very mature, and well-respected, international financial organization.

Thank you!

```html
<!DOCTYPE html>
<html lang="en">
<head>
<meta charset="utf-8">
<title>Unitdesk – My View</title>
<link href="https://fonts.googleapis.com/css2?family=Roboto:wght@400;500;700&display=swap" rel="stylesheet">
<style>
:root{
  --green:#8dc63f;--orange:#f28c28;--blue:#2ea3dc;--grey:#8c8c8c;
  --nav:#9b9b9b;--footer:#5e5e5e;--text:#555;--line:#e2e2e2;--bg:#f4f4f4;--teal:#2fc59a;
}
*{box-sizing:border-box;margin:0;padding:0}
html,body{width:1195px;height:1200px;overflow:hidden}
body{font-family:Roboto,Arial,sans-serif;background:var(--bg);color:var(--text);position:relative;font-size:11px}
.abs{position:absolute}
.header{left:0;top:0;width:1195px;height:98px;background:linear-gradient(#fff,#ececec)}
.brand{left:0;top:0;width:191px;height:98px;background:#fff;box-shadow:2px 2px 6px rgba(0,0,0,.15);display:flex;align-items:center;padding-left:20px;gap:8px}
.brand-mark{width:26px;height:26px;border-radius:50%;background:var(--orange)}
.brand-name{font-size:20px;font-weight:500;color:#666}
.tab{top:35px;height:37px;color:#fff;font-size:11px;font-weight:500;display:flex;align-items:center;justify-content:center}
.global{left:691px;top:36px;width:294px;height:36px;border:1px solid #ccc;background:#f7f7f7;display:flex;align-items:center;gap:24px;padding-left:20px;font-size:11px;color:#444;font-weight:500}
.greet{left:1000px;top:46px;font-size:10px;font-weight:500;color:#444;width:146px;text-align:right}
.greet b{color:var(--green);font-weight:500}
.avatar{border-radius:50%;background:linear-gradient(135deg,#d9b79a,#8f6c55)}
.subnav{left:0;top:120px;width:1195px;display:flex;justify-content:space-around;padding:0 70px;font-size:11px;font-weight:500;color:#555}
.panel{background:#fff;border:1px solid var(--line)}
.work-title{left:10px;top:158px;width:1173px;height:48px;border-bottom:1px solid var(--line);text-align:center;line-height:48px;font-size:18px;color:#777;font-weight:500}
.card{top:231px;height:253px;border:1px solid var(--line);background:#fafafa}
.card-head{height:42px;color:#fff;font-size:13px;font-weight:500;padding-left:15px;line-height:42px;white-space:nowrap}
.row{height:39.5px;border-bottom:1px solid var(--line);display:flex;align-items:center;padding:0 13px;font-size:11px;justify-content:space-between;gap:6px;white-space:nowrap}
.row .ic{width:12px;height:14px;border:1px solid #aaa;margin-right:8px;flex:none}
.row .name{flex:1}
.see{position:absolute;right:15px;bottom:12px;font-size:10px;text-decoration:underline;color:#555}
.navbar{left:10px;top:528px;width:1173px;height:49px;background:var(--nav);display:flex;align-items:center;padding:0 16px;font-size:10px;font-weight:500;color:#fff;justify-content:space-between;white-space:nowrap}
.block{background:#fff;border:1px solid var(--line)}
.conv{display:flex;gap:14px;padding:12px 10px 0;line-height:25px;font-size:11px}
.conv .avatar{width:34px;height:34px;flex:none;margin-top:2px}
.postbox{margin:14px 11px 0;height:50px;border:1px solid #ddd;background:#fafafa}
.post{margin:4px 11px 0 auto;width:55px;height:24px;background:var(--blue);color:#fff;font-size:11px;display:flex;align-items:center;justify-content:center;font-weight:500}
.list{padding:10px 15px 0}
.list li{list-style:none;height:41px;display:flex;align-items:center;gap:14px;font-size:11px;white-space:nowrap}
.tick{color:#999;font-size:11px}
.contact{display:flex;align-items:center;gap:14px;height:46px;padding-left:12px;font-size:11px}
.contact .avatar{width:37px;height:37px}
.news li{justify-content:space-between;gap:10px;font-size:10.5px}
.footer{left:0;top:1145px;width:1195px;height:55px;background:var(--footer);color:#fff;font-size:10px;font-weight:500;text-align:center;line-height:50px}
</style>
</head>
<body>
<header class="abs header"></header>
<div class="abs brand"><span class="brand-mark"></span><span class="brand-name">UNITDESK</span></div>
<div class="abs tab" style="left:340px;width:138px;background:var(--blue)">ENTERPRISE HOMEPAGE</div>
<div class="abs tab" style="left:482px;width:86px;background:var(--green)">DEPT. VIEW</div>
<div class="abs tab" style="left:573px;width:86px;background:var(--orange)">MY VIEW</div>
<nav class="abs global"><span>GLOBAL NAV :</span><span>LINK 1</span><span>LINK 2</span><span>LINK3</span></nav>
<div class="abs greet">GOOD MORNING <b>JANE!</b></div>
<div class="abs avatar" role="img" aria-label="Profile photo of Jane" style="left:1152px;top:37px;width:33px;height:33px"></div>

<nav class="abs subnav"><span>MY HR</span><span>|</span><span>MY TRAINING</span><span>|</span><span>MY BENEFITS</span><span>|</span><span>MY DEPENDENTS</span><span>|</span><span>MY HEALTH INSURANCE</span><span>|</span><span>MY SALARY</span></nav>

<section class="abs panel" style="left:10px;top:158px;width:1173px;height:356px"></section>
<h1 class="abs work-title">MY WORK</h1>

<div class="abs card" style="left:24px;width:242px">
  <div class="card-head" style="background:var(--green)">MY RECENT DOCS</div>
  <div class="row"><span class="ic"></span><span class="name">Document file name 1</span><span>04/07/2017</span></div>
  <div class="row"><span class="ic"></span><span class="name">Spreadsheet file name 2</span><span>03/07/2017</span></div>
  <div class="row"><span class="ic"></span><span class="name">PDF document file 3</span><span>02/07/2017</span></div>
  <div class="row"><span class="ic"></span><span class="name">Document file name 1</span><span>01/07/2017</span></div>
  <div class="row" style="border:0"><span class="ic"></span><span class="name">Spreadsheet file name 2</span><span>04/07/2017</span></div>
</div>
<div class="abs card" style="left:291px;width:292px">
  <div class="card-head" style="background:var(--orange)">MY RECENT EMAILS</div>
  <div class="row"><span style="width:110px">Lorem ipsum dolor</span><span class="name">Robin Talbot</span><span>9:23 am</span></div>
  <div class="row"><span style="width:110px">Et donec ligula feug</span><span class="name">Jana Arvel</span><span>8:30 am</span></div>
  <div class="row"><span style="width:110px">Dapibus imperdiet</span><span class="name">Jonas Medley</span><span>8:22 am</span></div>
  <div class="row"><span style="width:110px">Lorem ipsum dolor</span><span class="name">Robin Talbot</span><span>7:43 am</span></div>
  <div class="row" style="border:0"><span style="width:110px">Duis vel eu velit</span><span class="name">Jorin Kalde</span><span>12:30 am</span></div>
</div>
<div class="abs card" style="left:610px;width:243px">
  <div class="card-head" style="background:var(--blue)">MY UPCOMING MEETINGS</div>
  <div class="row" style="justify-content:flex-start"><span style="width:77px">Meeting 1</span><span style="width:95px">HQ2 7B-073</span><span>2:30pm</span></div>
  <div class="row" style="justify-content:flex-start"><span style="width:77px">Meeting 2</span><span style="width:95px">HQ2 7B-073</span><span>2:30pm</span></div>
  <div class="row" style="justify-content:flex-start"><span style="width:77px">Meeting 3</span><span style="width:95px">HQ2 7B-073</span><span>2:30pm</span></div>
  <div class="row" style="justify-content:flex-start"><span style="width:77px">Meeting 4</span><span style="width:95px">HQ2 7B-073</span><span>2:30pm</span></div>
</div>
<div class="abs card" style="left:879px;width:291px">
  <div class="card-head" style="background:var(--grey)">MY TASKS</div>
  <div class="row"><span class="name">Review Georgia's 2017 Country Report</span><span>01/07/2017</span></div>
  <div class="row"><span class="name">Submit Conference Selections</span><span>04/07/2017</span></div>
  <div class="row"><span class="name">Complete stability chapter 2 analysis</span><span>03/07/2017</span></div>
  <span class="see">SEE ALL</span>
</div>

<nav class="abs navbar"><span>MY NAVIGATION :</span><span>CREATE NEW DOCUMENT</span><span>|</span><span>CREATE NEW SPREADSHEET</span><span>|</span><span>CREATE NEW EMAIL MESSAGE</span><span>|</span><span>SCHEDULE A MEETING</span><span>|</span><span>CREATE NEW TASK</span><span>|</span><span>BOOK TRAVEL</span><span>|</span><span>SUBMIT EXPENSES</span></nav>

<section class="abs block" style="left:10px;top:602px;width:368px;height:495px">
  <div class="card-head" style="background:var(--orange)">MY RECENT CONVERSATIONS</div>
  <div class="conv"><span class="avatar" role="img" aria-label="Colleague photo"></span><p>Lorem ipsum dolor sit amet, et donec ligula feugiat, tempor quis consectetuer ipsum... <svg width="14" height="13" viewBox="0 0 14 13"><path d="M1 6h3v6H1zM4 6l3-5c1 0 2 1 1.5 3H12c1 0 1.5 1 1 2l-1.5 5H4" fill="none" stroke="#888"/></svg></p></div>
  <div class="conv"><span class="avatar" role="img" aria-label="Colleague photo"></span><p>Lorem ipsum dolor sit amet, et donec ligula feugiat, tempor quis consectetuer ipsum... <svg width="15" height="13" viewBox="0 0 15 13"><path d="M7.5 13L1 6.5C-1 3.5 2-1 5 1l2.5 2L10 1c3-2 6 2.5 4 5.5z" fill="#e8452c"/></svg></p></div>
  <div class="postbox"></div><div class="post">POST</div>
  <div class="conv"><span class="avatar" role="img" aria-label="Colleague photo"></span><p>Lorem ipsum dolor sit amet, et donec ligula feugiat, tempor quis consectetuer ipsum...</p></div>
  <div class="conv"><span class="avatar" role="img" aria-label="Colleague photo"></span><p>Lorem ipsum dolor sit amet, et donec ligula feugiat, tempor quis consectetuer ipsum... <svg width="14" height="13" viewBox="0 0 14 13"><path d="M1 6h3v6H1zM4 6l3-5c1 0 2 1 1.5 3H12c1 0 1.5 1 1 2l-1.5 5H4" fill="none" stroke="#888"/></svg></p></div>
  <div class="postbox"></div><div class="post">POST</div>
</section>

<section class="abs block" style="left:390px;top:602px;width:287px;height:238px">
  <div class="card-head" style="background:var(--green)">MY TEAMS/COMMUNITIES</div>
  <ul class="list">
    <li><span class="tick">✔</span>Bulgaria - June 2017 Mission</li>
    <li><span class="tick">✔</span>Romania - April 2016 Mission</li>
    <li><span class="tick">✔</span>Bulgaria Country Team</li>
    <li><span class="tick">✔</span>Macedonia Country Team</li>
  </ul>
  <span class="see" style="color:var(--green);bottom:10px">SEE ALL</span>
</section>

<section class="abs block" style="left:390px;top:859px;width:287px;height:237px">
  <div class="card-head" style="background:var(--grey)">MY COLLEAGUES / FREQUENT CONTACTS</div>
  <div style="padding-top:7px">
    <div class="contact"><span class="avatar" role="img" aria-label="Contact photo"></span>Robin Talbot, Mission Chief</div>
    <div class="contact"><span class="avatar" role="img" aria-label="Contact photo"></span>Chen Lio, Senior Economist</div>
    <div class="contact"><span class="avatar" role="img" aria-label="Contact photo"></span>Osric Mulenga, Resident Rep</div>
    <div class="contact"><span class="avatar" role="img" aria-label="Contact photo"></span>Jorin Kalde, Desk Economist</div>
  </div>
</section>

<section class="abs block" style="left:690px;top:602px;width:494px;height:206px">
  <div class="card-head" style="background:var(--blue)">MY NEWS REPORTS</div>
  <ul class="list news">
    <li><span class="tick">✔</span><span style="flex:1">Banks' Preparations for Brexit Need to Improve - CRB, NRB (Ledgerwire) 11:32 am</span><span>04/07/2017</span></li>
    <li><span class="tick">✔</span><span style="flex:1">Eurozone recovery broadening but gaps remain (Meridian Press) &nbsp; 9:03 am</span><span>01/07/2017</span></li>
    <li><span class="tick">✔</span><span style="flex:1">Lorem ipsum dolor sit amet, et donec ligula feugiat, tempor quis co... 5:45 pm</span><span>01/07/2017</span></li>
  </ul>
  <span class="see" style="color:var(--blue);bottom:8px;right:18px">SEE ALL</span>
</section>

<section class="abs block" style="left:690px;top:820px;width:494px;height:276px">
  <div class="card-head" style="background:var(--orange)">MY ANALYTICS</div>
  <svg class="abs" style="left:8px;top:84px" width="188" height="147" viewBox="0 0 188 147" font-family="Roboto,sans-serif" font-size="5" fill="#888">
    <rect x=".5" y=".5" width="187" height="146" fill="#fff" stroke="#ddd"/>
    <text x="7" y="10">SUBSCRIPTIONS :</text>
    <rect x="152" y="6" width="28" height="8" fill="none" stroke="#ccc"/><text x="155" y="12">Months</text>
    <g stroke="#eee"><line x1="20" y1="28" x2="180" y2="28"/><line x1="20" y1="49" x2="180" y2="49"/><line x1="20" y1="70" x2="180" y2="70"/><line x1="20" y1="91" x2="180" y2="91"/><line x1="20" y1="112" x2="180" y2="112"/><line x1="20" y1="133" x2="180" y2="133"/></g>
    <text x="6" y="30">500</text><text x="6" y="51">400</text><text x="6" y="72">300</text><text x="6" y="93">200</text><text x="6" y="114">100</text>
    <g fill="var(--teal)"><rect x="34" y="66" width="9" height="67"/><rect x="56" y="102" width="9" height="31"/><rect x="77" y="120" width="9" height="13"/><rect x="98" y="111" width="9" height="22"/><rect x="120" y="91" width="9" height="42"/><rect x="141" y="73" width="9" height="60"/><rect x="162" y="38" width="9" height="95"/></g>
    <text x="34" y="141">Jan</text><text x="56" y="141">Feb</text><text x="77" y="141">Mar</text><text x="98" y="141">Apr</text><text x="120" y="141">May</text><text x="141" y="141">Jun</text><text x="163" y="141">Jul</text>
  </svg>
  <svg class="abs" style="left:206px;top:122px" width="82" height="82" viewBox="0 0 82 82">
    <g fill="none" stroke-width="5">
      <circle cx="41" cy="41" r="37" stroke="#f2d78b"/>
      <path d="M41 4A37 37 0 0 0 14 15" stroke="var(--green)"/>
      <path d="M14 15A37 37 0 0 0 8 58" stroke="var(--orange)"/>
      <path d="M8 58A37 37 0 0 0 26 75" stroke="var(--blue)"/>
      <path d="M26 75A37 37 0 0 0 56 75" stroke="#9a84d8"/>
    </g>
  </svg>
  <svg class="abs" style="left:297px;top:84px" width="188" height="147" viewBox="0 0 188 147" font-family="Roboto,sans-serif" font-size="5" fill="#888">
    <rect x=".5" y=".5" width="187" height="146" fill="#fff" stroke="#ddd"/>
    <text x="7" y="10">VISITORS :</text>
    <rect x="160" y="6" width="20" height="8" fill="none" stroke="#ccc"/><text x="163" y="12">Days</text>
    <g stroke="#eee"><line x1="20" y1="28" x2="180" y2="28"/><line x1="20" y1="49" x2="180" y2="49"/><line x1="20" y1="70" x2="180" y2="70"/><line x1="20" y1="91" x2="180" y2="91"/><line x1="20" y1="112" x2="180" y2="112"/><line x1="20" y1="133" x2="180" y2="133"/></g>
    <text x="6" y="30">500</text><text x="6" y="51">400</text><text x="6" y="72">300</text><text x="6" y="93">200</text><text x="6" y="114">100</text>
    <polyline points="40,55 70,80 90,75 102,94 143,92 170,76" fill="none" stroke="#aaa" stroke-width=".7"/>
    <g fill="var(--teal)"><circle cx="40" cy="55" r="1.6"/><circle cx="70" cy="80" r="1.6"/><circle cx="90" cy="75" r="3"/><circle cx="102" cy="94" r="1.6"/><circle cx="143" cy="92" r="1.6"/><circle cx="170" cy="76" r="1.6"/></g>
    <rect x="76" y="60" width="28" height="8" fill="#fff" stroke="#ccc"/><text x="79" y="66">Wed - 275</text>
    <text x="34" y="141">Mon</text><text x="58" y="141">Tue</text><text x="82" y="141">Wed</text><text x="106" y="141">Thu</text><text x="130" y="141">Fri</text><text x="151" y="141">Sat</text><text x="171" y="141">Sun</text>
  </svg>
</section>

<footer class="abs footer">© COPY RIGHT 2017 UNITDESK. ALL RIGHTS RESERVED.</footer>
</body>
</html>
```